QLDR Individual and Corporate Development Business Card Design

QLDR needs a business card design that is aligned with it's values and targetted markets. Harmonic Ladder of Reasoning Matrix's self diagnosis model and tools, which can be used for personal improvement and team/business performance enhancement, is based on the learnings of over 20 years of medical practitioning. QLDR supercharges personal effectiveness and awareness to also increase team and business performance.

The targetted markets are high performance individuals and teams who aspire seek to enhance their capabilities and achieve their absolute best potential.

Look and feel for the business card design we are looking for is high technology, premium, fresh, new and medical.

Target Market(s)

Industry/Entity Type

Business Consultant

Contact Information for Business Card

Logo, Full Name, Title, Phone number, Email, company name, Address,

Font styles to use
Sans Serif

Requirements
Must have
• Tag line: Maximising Performance for Highly Effective People
• Please use same colours as the logo.

```html
<!DOCTYPE html>
<html lang="en">
<head>
<meta charset="utf-8">
<title>QLDR Business Card</title>
<link href="https://fonts.googleapis.com/css2?family=Open+Sans:wght@400;600;700&display=swap" rel="stylesheet">
<style>
  :root {
    --teal: #1aa7c1;
    --ink: #3c3c3c;
    --muted: #8a9096;
    --rule: #d4d6d8;
    --rule-dark: #3a3d42;
    --card-light: #ffffff;
    --card-dark: #08090b;
    --backdrop: #8c8c8c;
  }
  * { margin: 0; padding: 0; box-sizing: border-box; }
  html, body { width: 1200px; height: 1000px; overflow: hidden; }
  body {
    background: var(--backdrop);
    font-family: "Open Sans", Arial, sans-serif;
    position: relative;
  }
  .card {
    position: absolute;
    left: 348px;
    width: 515px;
  }
  .card--front { top: 148px; height: 305px; background: var(--card-light); }
  .card--back  { top: 530px; height: 303px; background: var(--card-dark); }

  .brand-name {
    position: absolute;
    font-weight: 700;
    color: var(--teal);
    line-height: 1;
    white-space: nowrap;
  }
  .brand-full {
    position: absolute;
    font-weight: 600;
    color: var(--teal);
    text-transform: uppercase;
    line-height: 1.15;
    white-space: nowrap;
  }
  .rule { position: absolute; height: 2px; }

  .card--front .brand-name { left: 48px; top: 66px; font-size: 46px; letter-spacing: 9px; }
  .card--front .rule { left: 30px; top: 114px; width: 452px; background: var(--rule); }
  .card--front .brand-full { left: 48px; top: 118px; font-size: 12.5px; letter-spacing: 1.2px; }

  .person { position: absolute; right: 33px; top: 88px; text-align: right; }
  .person__name { color: var(--teal); font-size: 18px; font-weight: 600; }
  .person__title { color: var(--ink); font-size: 12.5px; margin-top: 9px; }

  .contact {
    position: absolute; right: 33px; top: 178px;
    text-align: right; color: var(--ink); font-size: 12.5px; line-height: 15px;
  }
  .contact__address { margin-bottom: 14px; }
  .contact__line { display: flex; justify-content: flex-end; align-items: center; gap: 4px; height: 17px; }
  .contact__line svg { width: 10px; height: 10px; fill: var(--teal); }

  .card--back .brand-name {
    left: 0; right: 0; text-align: center; top: 112px;
    font-size: 66px; letter-spacing: 14px; padding-left: 14px;
  }
  .card--back .rule { left: 110px; top: 185px; width: 294px; background: var(--rule-dark); }
  .card--back .brand-full { left: 138px; top: 190px; font-size: 17.5px; letter-spacing: 2px; }

  .tagline {
    position: absolute; left: 0; right: 0; top: 262px;
    text-align: center; color: var(--muted);
    font-size: 11px; font-weight: 400; letter-spacing: 1px;
  }
</style>
</head>
<body>
  <section class="card card--front">
    <div class="brand-name">QLDR</div>
    <div class="rule"></div>
    <div class="brand-full">Harmonic Ladder<br>of Reasoning Matrix</div>

    <div class="person">
      <div class="person__name">Dana Whitfield</div>
      <div class="person__title">General Manager</div>
    </div>

    <div class="contact">
      <div class="contact__address">12 Larch Row, Eastmere<br>P.O. Box 410, 7 Birch Ave</div>
      <div class="contact__line">555-0142-7730
        <svg viewBox="0 0 10 10"><path d="M2 0.5 L4 2.5 L3 3.8 Q4.5 6 6.2 7 L7.5 6 L9.5 8 L8 9.6 Q3.5 9 0.4 2 Z"/></svg>
      </div>
      <div class="contact__line">hello@qldr-dev.com
        <svg viewBox="0 0 10 10"><path d="M0 2 H10 V8.5 H0 Z M0.6 2.4 L5 5.6 L9.4 2.4" stroke="#fff" stroke-width="0.8"/></svg>
      </div>
      <div class="contact__line">www.qldr-dev.com
        <svg viewBox="0 0 10 10"><circle cx="5" cy="5" r="4.5" fill="none" stroke="var(--teal)" stroke-width="1"/><path d="M0.5 5 H9.5 M5 0.5 V9.5" stroke="var(--teal)" stroke-width="0.8"/></svg>
      </div>
    </div>
  </section>

  <section class="card card--back">
    <div class="brand-name">QLDR</div>
    <div class="rule"></div>
    <div class="brand-full">Harmonic Ladder<br>of Reasoning Matrix</div>
    <p class="tagline">Maximising Performance for Highly Effective People</p>
  </section>
</body>
</html>
```